Rivolex.com Trucking Company Website

Need a website designed (no content) for a trucking company, specializing in trucking of ocean containers (intermodal Trucking). Heavy emphasis on technology, using latest technology, providing unabated visibility and realtime information.
clean minimalist industrial website
example:
https://www.bramtiq.com/

Target Market(s)

Professional Business Consumer corporate and small business

Industry/Entity Type

Trucking Company

Number of Pages Required

5+ page

Requirements
Must have
• Industrial Design, simple informative, for a busy professional to view and get the necessary information with out the distractions.
• Blog Page
• Client Log-In on the front page
• Technology page - showing our intensive investments in technology
Nice to have
• If ANY images included, MUST be USA related. Example if include an image of a truck, ensure its a USA model. Do the research.
• included our business card for sample of Logo
• Doesnt not have to be the same color schemes.
Should not have
• moving images

```html
<!DOCTYPE html>
<html lang="en">
<head>
<meta charset="utf-8">
<title>Rivolex.com – Intermodal Trucking</title>
<link rel="stylesheet" href="https://fonts.googleapis.com/css2?family=Montserrat:wght@400;600;700&family=Mulish:wght@400;600;700&display=swap">
<style>
  :root {
    --blue: #2b73b8;
    --blue-dark: #1f5e9c;
    --orange: #f7941d;
    --orange-soft: #f8a43c;
    --ink: #222;
    --text-grey: #6f6f6f;
    --muted: #a9a9a9;
    --white: #fff;
    --band: #4d4f54;
  }
  * { box-sizing: border-box; margin: 0; padding: 0; }
  html, body { width: 1093px; height: 1200px; overflow: hidden; }
  body { position: relative; font-family: "Mulish", sans-serif; color: var(--ink); background: var(--white); }
  .abs { position: absolute; }

  /* top bar */
  .topbar { left: 0; top: 0; width: 1093px; height: 33px; background: var(--blue); color: var(--white); font-family: "Montserrat", sans-serif; font-size: 9px; letter-spacing: 1.6px; }
  .topbar .phone { position: absolute; left: 78px; top: 10px; display: flex; align-items: center; gap: 12px; }
  .topbar .address { position: absolute; right: 79px; top: 10px; letter-spacing: 1.1px; }

  /* header */
  .header { left: 0; top: 33px; width: 1093px; height: 71px; background: var(--white); }
  .brand { position: absolute; left: 77px; top: 17px; display: flex; align-items: center; gap: 8px; font-family: "Montserrat", sans-serif; font-weight: 700; font-size: 30px; color: var(--blue-dark); letter-spacing: 1px; }
  .brand .mark { width: 14px; height: 14px; background: var(--blue-dark); }
  .nav { position: absolute; top: 0; left: 0; }
  .nav .home { position: absolute; left: 464px; top: 20px; width: 30px; height: 30px; border-radius: 50%; background: var(--blue); display: flex; align-items: center; justify-content: center; }
  .nav a { position: absolute; top: 29px; font-family: "Montserrat", sans-serif; font-size: 11px; letter-spacing: 2px; color: #555; text-decoration: none; }
  .btn-register { position: absolute; left: 901px; top: 15px; width: 112px; height: 40px; background: var(--blue); color: var(--white); font-family: "Montserrat", sans-serif; font-weight: 700; font-size: 12px; display: flex; align-items: center; justify-content: center; border-radius: 2px; }

  /* hero */
  .hero { left: 0; top: 104px; width: 1093px; height: 362px; background: var(--orange); }
  .hero-art { position: absolute; left: 80px; top: 26px; width: 530px; height: 282px; border-radius: 8px; background: radial-gradient(circle at 30% 60%, #e8641f 0%, #ed7a1f 40%, rgba(247,148,29,0) 72%); }
  .hero-title { position: absolute; left: 637px; top: 48px; font-family: "Montserrat", sans-serif; font-weight: 700; font-size: 31px; line-height: 38px; color: var(--white); letter-spacing: 0.5px; }
  .field { position: absolute; left: 637px; width: 376px; height: 40px; border: 2px solid #fbc68a; background: var(--orange-soft); color: var(--white); font-size: 12px; padding: 9px 11px; }
  .btn-login { position: absolute; left: 637px; top: 262px; width: 111px; height: 40px; border: 2px solid #fbd9b0; background: #f3ad5e; color: var(--white); font-family: "Montserrat", sans-serif; font-weight: 700; font-size: 11px; display: flex; align-items: center; justify-content: center; border-radius: 2px; }
  .dots { position: absolute; left: 327px; top: 327px; display: flex; gap: 5px; }
  .dots span { width: 9px; height: 9px; border-radius: 50%; background: var(--white); }
  .dots span.ring { background: transparent; border: 1.5px solid var(--white); }

  /* about */
  .about { left: 0; top: 466px; width: 1093px; height: 582px; }
  .about-map { position: absolute; left: 10px; top: 40px; width: 1073px; height: 480px; border-radius: 40%; background: radial-gradient(ellipse at center, #f3f3f3 0%, #f8f8f8 55%, rgba(255,255,255,0) 75%); }
  .section-title { position: absolute; left: 0; width: 1093px; top: 40px; text-align: center; font-family: "Montserrat", sans-serif; font-weight: 700; font-size: 20px; letter-spacing: 7px; color: #111; }
  .section-rule { position: absolute; left: 530px; top: 74px; width: 34px; height: 3px; background: var(--blue); }
  .section-lede { position: absolute; left: 0; width: 1093px; top: 92px; text-align: center; font-size: 12px; color: var(--muted); }
  .device { position: absolute; left: 452px; top: 150px; width: 188px; height: 384px; border-radius: 24px; background: linear-gradient(180deg, #2a2a2a, #111); }
  .device-screen { position: absolute; left: 11px; top: 46px; width: 166px; height: 290px; background: linear-gradient(180deg, #ffffff 0%, #fbeaea 60%, #e23b3b 100%); }

  .service { position: absolute; width: 300px; }
  .service .icon { position: absolute; top: 0; width: 49px; height: 49px; border-radius: 50%; background: var(--blue); display: flex; align-items: center; justify-content: center; }
  .service .name { position: absolute; top: 17px; font-family: "Montserrat", sans-serif; font-weight: 600; font-size: 12px; color: #111; white-space: nowrap; }
  .service p { position: absolute; top: 57px; font-size: 10px; line-height: 21px; letter-spacing: 0.5px; color: var(--text-grey); width: 300px; }
  .service.left .icon { right: 0; }
  .service.left .name { right: 63px; }
  .service.left p { right: 0; text-align: right; }
  .service.right .icon { left: 0; }
  .service.right .name { left: 62px; }
  .service.right p { left: 0; text-align: left; width: 280px; }
  .service .name.active { color: var(--blue); border-bottom: 1px solid var(--blue); padding-bottom: 1px; }

  /* technology */
  .tech { left: 0; top: 1048px; width: 1093px; height: 152px; overflow: hidden; background: linear-gradient(90deg, #5a5c62 0%, #7c8088 55%, #a9acb2 100%); }
  .tech-photo { position: absolute; left: 430px; top: 0; width: 663px; height: 152px; background: linear-gradient(160deg, #c8cbd0 0%, #8f949b 50%, #4d5158 100%); }
  .tech-panel { position: absolute; left: 0; top: 0; width: 1093px; height: 152px; background: var(--band); clip-path: polygon(0 0, 395px 0, 555px 152px, 0 152px); opacity: 0.96; }
  .tech-title { position: absolute; left: 80px; top: 46px; color: var(--white); font-family: "Montserrat", sans-serif; font-size: 29px; line-height: 40px; font-weight: 400; }
  .tech-title strong { font-weight: 700; }
  .tech-lede { position: absolute; left: 75px; top: 131px; color: #e6e6e6; font-size: 11px; letter-spacing: 0.6px; }
</style>
</head>
<body>

<div class="abs topbar">
  <div class="phone">
    <svg width="11" height="11" viewBox="0 0 24 24" fill="none" stroke="#9cc0e6" stroke-width="2"><path d="M22 16.9v3a2 2 0 0 1-2.2 2 19.8 19.8 0 0 1-8.6-3.1 19.5 19.5 0 0 1-6-6A19.8 19.8 0 0 1 2.1 4.2 2 2 0 0 1 4.1 2h3a2 2 0 0 1 2 1.7c.1.9.4 1.8.7 2.7a2 2 0 0 1-.5 2.1L8 9.8a16 16 0 0 0 6 6l1.3-1.3a2 2 0 0 1 2.1-.4c.9.3 1.8.6 2.7.7a2 2 0 0 1 1.7 2z"/></svg>
    <span>000-000-000</span>
  </div>
  <div class="address">2930 LOREM IPSUM IS SIMPLY DUMMY TEXT OF THE M2B 4R9</div>
</div>

<header class="abs header">
  <div class="brand"><span class="mark"></span>RIVOLEX</div>
  <nav class="nav">
    <div class="home">
      <svg width="11" height="11" viewBox="0 0 24 24" fill="#fff"><path d="M12 3 2 12h3v8h5v-6h4v6h5v-8h3z"/></svg>
    </div>
    <a style="left:523px">ABOUT</a>
    <a style="left:607px">TECHNOLOGY</a>
    <a style="left:741px">BLOG</a>
    <a style="left:814px">CONTACT</a>
  </nav>
  <div class="btn-register">Register</div>
</header>

<section class="abs hero">
  <div class="hero-art" role="img" aria-label="Illustration of delivery trucks with a world map, a checklist and 24-hour service arrows"></div>
  <h1 class="hero-title">DEPENDABLE<br>TRANSPORTATION</h1>
  <div class="field" style="top:143px">username</div>
  <div class="field" style="top:198px">password</div>
  <div class="btn-login">Log-In</div>
  <div class="dots"><span class="ring"></span><span></span><span></span></div>
</section>

<section class="abs about">
  <div class="about-map" role="img" aria-label="Faint world map background"></div>
  <h2 class="section-title">ABOUT</h2>
  <div class="section-rule"></div>
  <p class="section-lede">Lorem Ipsum is simply dummy text of the printing and typesetting industry.</p>

  <div class="device" role="img" aria-label="Smartphone showing the company name and a red American semi truck">
    <div class="device-screen"></div>
  </div>

  <div class="service left" style="left:99px; top:190px; height:120px">
    <div class="icon">
      <svg width="28" height="20" viewBox="0 0 28 20" fill="none" stroke="#fff" stroke-width="1.5"><rect x="1" y="3" width="17" height="11" rx="1"/><path d="M18 6h5l4 4v4h-9z"/><circle cx="6" cy="16" r="2.2"/><circle cx="22" cy="16" r="2.2"/></svg>
    </div>
    <div class="name active">Transportation</div>
    <p>Lorem Ipsum is simply dummy text of the printing and typesetting industry. Lorem Ipsum has been the industry's standard dummy text</p>
  </div>

  <div class="service left" style="left:99px; top:357px; height:120px">
    <div class="icon">
      <svg width="28" height="22" viewBox="0 0 28 22" fill="none" stroke="#fff" stroke-width="1.5"><rect x="2" y="3" width="13" height="11"/><path d="M15 7h6l5 5v4H15z"/><circle cx="6" cy="18" r="2.2"/><circle cx="21" cy="18" r="2.2"/><path d="M5 3V1M9 3V1"/></svg>
    </div>
    <div class="name">Towing</div>
    <p>Lorem Ipsum is simply dummy text of the printing and typesetting industry. Lorem Ipsum has been the industry's standard....</p>
  </div>

  <div class="service right" style="left:694px; top:192px; height:120px">
    <div class="icon">
      <svg width="30" height="20" viewBox="0 0 30 20" fill="#fff"><path d="M10 3h19v11H10z"/><path d="M1 9l4-5h4v10H1z"/><circle cx="5" cy="16" r="2.4"/><circle cx="24" cy="16" r="2.4"/></svg>
    </div>
    <div class="name">Rental</div>
    <p>Lorem Ipsum is simply dummy text of the printing and typesetting industry. Lorem Ipsum has been the industry'...</p>
  </div>

  <div class="service right" style="left:694px; top:356px; height:120px">
    <div class="icon">
      <svg width="26" height="26" viewBox="0 0 24 24" fill="none" stroke="#fff" stroke-width="1.3"><circle cx="12" cy="12" r="3.5"/><path d="M19.4 15a1.7 1.7 0 0 0 .3 1.8l.1.1a2 2 0 1 1-2.8 2.8l-.1-.1a1.7 1.7 0 0 0-2.9 1.2V21a2 2 0 1 1-4 0v-.1a1.7 1.7 0 0 0-2.9-1.2l-.1.1a2 2 0 1 1-2.8-2.8l.1-.1A1.7 1.7 0 0 0 3 15a1.7 1.7 0 0 0-1.5-1H1.4a2 2 0 1 1 0-4h.1A1.7 1.7 0 0 0 3 9a1.7 1.7 0 0 0-.3-1.8l-.1-.1a2 2 0 1 1 2.8-2.8l.1.1A1.7 1.7 0 0 0 9 3.1V3a2 2 0 1 1 4 0v.1a1.7 1.7 0 0 0 2.9 1.2l.1-.1a2 2 0 1 1 2.8 2.8l-.1.1a1.7 1.7 0 0 0-.3 1.8 1.7 1.7 0 0 0 1.5 1h.1a2 2 0 1 1 0 4h-.1a1.7 1.7 0 0 0-1.5 1z"/></svg>
    </div>
    <div class="name">Other Services</div>
    <p>Lorem Ipsum is simply dummy text of the printing and typesetting industry. Lorem Ipsum has been the industry's standard dummy texte...</p>
  </div>
</section>

<section class="abs tech">
  <div class="tech-photo" role="img" aria-label="Photograph of a white American semi truck on the road at dusk"></div>
  <div class="tech-panel"></div>
  <h2 class="tech-title">TECHNOLOGY<br><strong>dummy</strong> text of the printing</h2>
  <p class="tech-lede">Lorem Ipsum is simply dummy text of the printing and typesetting industry.</p>
</section>

</body>
</html>
```